International oil and gas consultancy business needs a web design

Hello, I need a web design for a new oil and gas auditing consultancy business. My business undertakes contract audit assignments to review past costs of oil and gas operations (see attached Excel file for more details of the businesses services). I need the design to give the impression of a professional consultancy style of business, rather than a retail style of website. Note: this job is for LAYOUT DESIGN ONLY and not coding / development work.
The following are my key design principles:
1. BASIC DESIGN: I am after a simple and static web design. I don't want the pages busy or cluttered with too many images or detail.
2. HORIZONTAL TABS: I require a horizontal set of tabs towards the top of the screens (see Excel file) which remain in the same position on every page.
3. META TAG PLANNING: The design should allow for effective positioning of content so that key meta tag words can easily be built during the technical build stage.
4. NUMBER OF PAGES: The site will eventually have a maximum of 10 pages. Seven of the pages will reside under the tabs. Can you please present your opening submission for the first two page.
5. USE OF MY LOGO: The attached logo (JPEG file) should be used throughout the website. Please don't change the shape and colour.
6. COLOUR SCHEMES: Can you please consider any of the 3 colour schemes below:
A - dark red (to match the logo), light grey and perhaps another of your liking;
B - dark red (to match the logo), light cream and perhaps another of your liking;
C - dark red (to match the logo), white and perhaps another of your liking.
7. WORD CONTENT: I have attached an Excel file which shows the estimated word content for each page.
8. FUTURE USE OF DESIGN: I'm planning on building a Wordpress website. Can you please ensure the layout design supports this application.

Target Market(s)

oil and gas companies (small and large)

Industry/Entity Type

Oil And Gas

Font styles to use
Sans Serif

Requirements
Nice to have
• The KOL logo and business name should ideally be next to each other. Also, the logo and name should be part of the background graphics, not above it.

```html
<!DOCTYPE html>
<html lang="en">
<head>
<meta charset="utf-8">
<title>Kinross Oil Ledger — Audit Services</title>
<link rel="stylesheet" href="https://fonts.googleapis.com/css2?family=Source+Sans+3:wght@400;600;700&display=swap">
<style>
  :root{
    --brand-red:#8c1b20;
    --brand-blue:#1a4696;
    --slate:#4a4a4a;
    --link-blue:#1a5fd0;
    --mail-blue:#4a86d6;
    --name-blue:#1b4f80;
    --ink:#111;
    --muted:#444;
    --footer-grey:#d3d3d3;
    --white:#fff;
  }
  *{margin:0;padding:0;box-sizing:border-box}
  html,body{width:980px;height:1200px;overflow:hidden;background:var(--white)}
  body{font-family:"Source Sans 3",Arial,sans-serif;color:var(--ink)}
  .page{position:relative;width:1000px;height:1225px;transform:scale(.98);transform-origin:0 0}
  .abs{position:absolute}
  .top-rule{left:0;top:0;width:1000px;height:7px;background:var(--brand-red)}
  .contact-mail{left:441px;top:27px;font-size:17px;color:var(--mail-blue)}
  .contact-phone{left:682px;top:20px;font-size:27px;color:var(--brand-red)}
  .brand{left:88px;top:52px;width:170px;text-align:center}
  .brand-mark{font-size:54px;font-weight:700;color:var(--brand-red);line-height:1;letter-spacing:2px}
  .brand-name{font-size:14px;color:#777;margin-top:6px}
  .main-nav{left:275px;top:72px;width:641px;height:70px;background:var(--brand-red);display:flex}
  .main-nav a{color:var(--white);text-decoration:none;font-size:17px;display:flex;align-items:center;justify-content:center;border-right:1px solid rgba(255,255,255,.8)}
  .main-nav a:last-child{border-right:none}
  .hero{left:83px;top:143px;width:833px;height:384px;background:linear-gradient(180deg,#9fb3bf 0%,#e9d9a6 35%,#f4c560 55%,#b9a98b 75%,#5f7d3a 100%)}
  .hero-title{left:83px;top:220px;width:828px;text-align:center;font-size:26px;color:var(--ink)}
  .service-card{top:484px;width:244px;height:173px;padding:6px;color:var(--white)}
  .service-card .photo{height:115px}
  .service-card h2{font-weight:400;font-size:20px;text-align:center;margin-top:12px;text-transform:uppercase}
  .card-red{left:107px;background:var(--brand-red)}
  .card-red .photo{background:linear-gradient(135deg,#4a86d8,#8fb7ea)}
  .card-blue{left:376px;width:243px;background:var(--brand-blue)}
  .card-blue .photo{background:linear-gradient(135deg,#e9eef3,#9bb7d6)}
  .card-grey{left:647px;background:var(--slate)}
  .card-grey .photo{background:linear-gradient(135deg,#3f7fd0,#a9c7ea)}
  .intro{left:110px;top:685px;width:780px;text-align:center;font-size:18.5px;line-height:23px}
  .section-title{font-size:27px;font-weight:400;padding-bottom:4px;border-bottom:2px solid var(--brand-red)}
  .why{left:111px;top:790px;width:229px}
  .why .section-title{padding-left:8px}
  .why ul{list-style:none;margin-top:12px;padding-left:9px}
  .why li{display:flex;font-size:14.5px;line-height:18px;margin-bottom:8px}
  .why li svg{flex:none;margin:3px 6px 0 0}
  .read-more{font-weight:700;font-size:14.5px;color:var(--link-blue);text-decoration:none}
  .why .read-more{position:absolute;left:31px;top:198px}
  .reviews{left:378px;top:790px;width:513px}
  .review{display:flex;margin-top:14px}
  .review+.review{margin-top:16px}
  .review .avatar{width:64px;height:64px;flex:none;background:linear-gradient(180deg,#cfcfcf,#7d7d7d);margin-right:18px}
  .review h3{font-size:13px;font-weight:600;color:var(--name-blue)}
  .review p{font-size:12.5px;color:var(--muted);line-height:16px;margin-top:1px}
  .reviews .read-more{position:absolute;left:83px;top:201px}
  .footer{left:83px;top:1025px;width:833px;height:158px;background:var(--footer-grey);border-top:4px solid var(--brand-red)}
  .footer h4{position:absolute;top:20px;font-size:14.5px;font-weight:700;color:#444}
  .quick-links{position:absolute;left:53px;top:50px;list-style:none;font-size:13.5px;line-height:17px;color:#333}
  .partner-badge{position:absolute;left:235px;top:50px;width:76px;height:56px;background:#4d4a48}
  .social{position:absolute;left:370px;top:50px;display:grid;grid-template-columns:22px 22px;gap:4px 15px}
  .social span{width:22px;height:22px;border-radius:50%;background:#555}
  .footer-brand{position:absolute;left:615px;top:8px;width:180px;text-align:center}
  .footer-brand .brand-mark{font-size:42px}
  .footer-brand .brand-name{font-size:13px;color:#444;margin-top:2px}
  .copyright{position:absolute;left:539px;top:96px;font-size:14px;color:var(--brand-red)}
  .bottom-band{left:0;top:1183px;width:1000px;height:42px;background:var(--brand-red)}
</style>
</head>
<body>
<div class="page">
  <div class="abs top-rule"></div>
  <div class="abs contact-mail">admin@kinrossledger.example</div>
  <div class="abs contact-phone">+61 (0)400 318 652</div>

  <div class="abs brand">
    <div class="brand-mark">KOL</div>
    <div class="brand-name">Kinross Oil Ledger</div>
  </div>

  <nav class="abs main-nav">
    <a href="#" style="width:105px">About Us</a>
    <a href="#" style="width:84px">Services</a>
    <a href="#" style="width:119px">Our Partners</a>
    <a href="#" style="width:88px">Approch</a>
    <a href="#" style="width:134px">Why Choose Us</a>
    <a href="#" style="width:111px">Contact Us</a>
  </nav>

  <div class="abs hero" role="img" aria-label="Oil refinery towers against a golden sunset sky above green fields"></div>
  <h1 class="abs hero-title" style="font-weight:400">Quality audit services for the oil and gas industry.</h1>

  <div class="abs service-card card-red">
    <div class="photo" role="img" aria-label="Field worker in hard hat with clipboard beside an oil pump jack"></div>
    <h2>Joint Venture Audits</h2>
  </div>
  <div class="abs service-card card-blue">
    <div class="photo" role="img" aria-label="Two engineers in hard hats reviewing plans"></div>
    <h2>Contract Audits</h2>
  </div>
  <div class="abs service-card card-grey">
    <div class="photo" role="img" aria-label="Engineer with laptop at a drilling rig"></div>
    <h2>Operations Audits</h2>
  </div>

  <p class="abs intro">Kinross Oil Ledger is a Perth (Australia) based firm specialising in providing quality audit services for the oil and gas industry. Our skills and knowledge of oil and gas, along with a deep understanding of business commercial needs, ensures the high quality of our services</p>

  <section class="abs why">
    <h2 class="section-title">Why Us</h2>
    <ul>
      <li><svg width="13" height="12" viewBox="0 0 13 12"><path d="M1 6l4 4 7-9" fill="none" stroke="#8c1b20" stroke-width="2.6"/></svg>Cost savings</li>
      <li><svg width="13" height="12" viewBox="0 0 13 12"><path d="M1 6l4 4 7-9" fill="none" stroke="#8c1b20" stroke-width="2.6"/></svg>Risk Mitigation</li>
      <li><svg width="13" height="12" viewBox="0 0 13 12"><path d="M1 6l4 4 7-9" fill="none" stroke="#8c1b20" stroke-width="2.6"/></svg>Process Improvement</li>
      <li><svg width="13" height="12" viewBox="0 0 13 12"><path d="M1 6l4 4 7-9" fill="none" stroke="#8c1b20" stroke-width="2.6"/></svg>Contractual Efficiency &amp; Effrectiveness</li>
    </ul>
    <a class="read-more" href="#">Read more</a>
  </section>

  <section class="abs reviews">
    <h2 class="section-title">What Others Say</h2>
    <div class="review">
      <div class="avatar" role="img" aria-label="Client portrait"></div>
      <div><h3>Marco Pellin</h3><p>&nbsp;I feel that it’s critically important to know who you're dealing with when you make a lifestyle-creating investment.</p></div>
    </div>
    <div class="review">
      <div class="avatar" role="img" aria-label="Client portrait"></div>
      <div><h3>Marco Pellin</h3><p>&nbsp;I feel that it’s critically important to know who you're dealing with when you make a lifestyle-creating investment.</p></div>
    </div>
    <a class="read-more" href="#">Read more</a>
  </section>

  <footer class="abs footer">
    <h4 style="left:50px">Qucik Link</h4>
    <ul class="quick-links">
      <li>Home</li><li>Services</li><li>FAQ</li><li>Terms and Conditions</li><li>Privacy policy</li>
    </ul>
    <h4 style="left:235px">Our Partner</h4>
    <div class="partner-badge" role="img" aria-label="Partner badge"></div>
    <h4 style="left:370px">Follow Us</h4>
    <div class="social" aria-label="Social links">
      <span></span><span></span><span></span><span></span><span></span><span></span>
    </div>
    <div class="footer-brand">
      <div class="brand-mark">KOL</div>
      <div class="brand-name">Kinross Oil Ledger</div>
    </div>
    <div class="copyright">Copyright c&nbsp; 2014 Kinross Oil Ledger</div>
  </footer>

  <div class="abs bottom-band"></div>
</div>
</body>
</html>
```